I need a SEO-friendly Wordpress website (making sure to style H1, H2, H3, etc correctly) for a Hawaii-based law firm called Meridian Crest Legal Group. Comparable websites include https://trvlaw.example/ and https://www.boultem.example/ for design reference. The current copy on the WelbyCounsel.example website can be used.

Coding

```html
<!DOCTYPE html>
<html lang="en">
<head>
<meta charset="utf-8">
<title>Meridian Crest Legal Group – Divorce and Personal Injury Lawyers</title>
<link rel="stylesheet" href="https://fonts.googleapis.com/css2?family=Montserrat:wght@500;600;700&family=Open+Sans:wght@400;600;700&family=Noto+Serif:ital,wght@0,400;0,700;1,400&display=swap">
<style>
:root{
  --navy:#14256f;
  --gold:#b2852a;
  --gold-dark:#9c7322;
  --ink:#222;
  --text:#444;
  --rule:#e3e3e3;
  --footer:#0e1a30;
  --footer-deep:#0b1528;
  --white:#fff;
}
*{box-sizing:border-box;margin:0;padding:0}
html,body{width:1200px;height:2594px;overflow:hidden}
body{font-family:"Open Sans",sans-serif;color:var(--text);background:var(--white);position:relative}
.abs{position:absolute}
section,header,footer,nav,.band{position:absolute;left:0;width:1200px}

/* top bar */
.topbar{top:0;height:36px;background:var(--navy);color:var(--white);font-size:9.5px}
.topbar .mail{left:234px;top:12px;display:flex;gap:6px;align-items:center}
.topbar .addr{left:570px;top:12px;display:flex;gap:6px;align-items:center}
.topbar .direction{left:858px;top:0;width:342px;height:36px;background:var(--gold);clip-path:polygon(12px 0,100% 0,100% 100%,0 100%);font-family:Montserrat,sans-serif;font-weight:600;font-size:10.5px;padding:12px 0 0 26px;display:flex;gap:6px}

/* header */
.masthead{top:36px;height:82px;border-bottom:1px solid var(--rule)}
.brand{left:233px;top:28px}
.brand-name{font-family:Montserrat,sans-serif;font-weight:700;font-size:15.5px;color:var(--navy);letter-spacing:.2px}
.brand-tag{font-family:"Noto Serif",serif;font-style:italic;font-size:11.5px;color:var(--gold);margin-top:2px;letter-spacing:.4px}
.call{left:756px;top:20px;display:flex;gap:12px}
.call-ring{width:32px;height:32px;border:2px solid var(--gold);border-radius:50%;display:flex;align-items:center;justify-content:center;margin-top:5px}
.call-label{font-family:"Noto Serif",serif;font-style:italic;font-size:11.5px;color:var(--ink)}
.call-number{font-family:Montserrat,sans-serif;font-weight:700;font-size:18px;color:var(--gold);margin-top:2px}

/* nav */
.mainnav{top:118px;height:42px;border-bottom:1px solid var(--rule)}
.mainnav ul{list-style:none;display:flex;gap:27px;position:absolute;left:233px;top:16px;font-size:9.5px;color:var(--ink)}
.mainnav li.current{color:var(--gold)}
.mainnav .cta{left:803px;top:0;width:162px;height:42px;background:var(--gold);color:var(--white);font-family:Montserrat,sans-serif;font-weight:500;font-size:11px;text-align:center;line-height:44px}

/* hero */
.hero{top:160px;height:375px}
.hero-photo{width:100%;height:100%;background:linear-gradient(100deg,#a66a3a 0%,#6b4a36 22%,#3b4150 45%,#5a5f68 65%,#cfd2d6 85%,#ececec 100%)}
.hero-box{left:403px;top:95px;width:393px;height:188px;background:rgba(178,133,42,.94);color:var(--white);text-align:center}
.hero-box .frame{position:absolute;left:9px;top:9px;right:9px;bottom:9px;border:1px solid rgba(255,255,255,.8)}
.hero-box p{font-size:11px;font-weight:600;position:absolute;left:0;width:100%}
.hero-box h1{font-size:15px;font-weight:700;position:absolute;left:0;width:100%;top:80px;line-height:20px}

/* about */
.about{top:535px;height:407px}
.eyebrow-block{left:233px;top:60px;border-left:2px solid var(--navy);padding-left:14px;height:42px}
.eyebrow{font-family:Montserrat,sans-serif;font-weight:600;font-size:10.5px;color:var(--navy)}
.about h2{font-family:Montserrat,sans-serif;font-weight:600;font-size:19.5px;color:var(--ink);margin-top:5px}
.about h3{left:234px;top:130px;font-family:"Open Sans",sans-serif;font-weight:700;font-size:13.5px;color:var(--navy)}
.about .copy{left:234px;top:167px;width:420px;font-size:8.7px;line-height:15px;text-align:justify}
.about .copy p+p{margin-top:15px}
.btn-gold{left:234px;top:320px;width:128px;height:28px;background:var(--gold);color:var(--white);font-family:Montserrat,sans-serif;font-weight:600;font-size:8.5px;text-align:center;line-height:28px}
.enquiry{left:377px;top:312px;border-left:1px solid var(--rule);padding-left:13px;height:40px}
.enquiry .q{font-family:Montserrat,sans-serif;font-weight:600;font-size:9px;color:var(--ink)}
.enquiry .n{font-family:Montserrat,sans-serif;font-weight:700;font-size:13.5px;color:var(--gold);margin-top:5px}
.about-photo{left:671px;top:62px;width:294px;height:290px;background:linear-gradient(135deg,#2d323c,#6a6e74 45%,#c9c6c0 75%,#8c6a3c)}
.about-photo .frame{position:absolute;left:12px;top:12px;right:12px;bottom:12px;border:1px solid rgba(255,255,255,.85)}

/* consultation bands */
.band{height:156px;overflow:hidden}
.band-navy{top:942px;background:var(--navy)}
.band-gold{top:1946px;height:145px;background:var(--gold)}
.band .lead{left:233px;font-family:"Noto Serif",serif;font-size:17px;color:var(--white)}
.band .headline{left:233px;font-family:"Noto Serif",serif;font-weight:700;font-size:31px;color:var(--white);letter-spacing:.3px}
.band .phone-disc{width:48px;height:48px;border-radius:50%;display:flex;align-items:center;justify-content:center;left:666px}
.band .big-number{left:727px;font-family:"Noto Serif",serif;font-weight:700;font-size:30px;color:var(--white)}
.band svg.chev{position:absolute;left:0;top:0}

/* practice areas */
.practice{top:1098px;height:443px}
.section-eyebrow{left:0;width:1200px;top:58px;text-align:center;font-family:Montserrat,sans-serif;font-weight:600;font-size:10.5px;color:var(--gold)}
.section-eyebrow::before,.section-eyebrow::after{content:"";display:inline-block;width:36px;height:1px;background:var(--gold);vertical-align:middle;margin:0 14px}
.practice h2{left:0;width:1200px;top:76px;text-align:center;font-family:Montserrat,sans-serif;font-weight:600;font-size:19.5px;color:var(--ink)}
.area{top:135px;width:172px}
.area .pic{width:169px;height:144px}
.area h3{font-family:Montserrat,sans-serif;font-weight:700;font-size:11px;color:var(--ink);margin-top:17px;line-height:15px}
.area p{font-size:8.7px;line-height:15px;margin-top:7px}

/* map */
.map{top:1541px;height:405px}
.map-fill{width:100%;height:100%;background:linear-gradient(90deg,#a9cdf0 0%,#b6d4f1 22%,#e6e6e3 30%,#eeeeec 60%,#e9e9e7 100%)}
.map-card{left:412px;top:117px;width:187px;height:132px;background:var(--white);border-radius:3px;box-shadow:0 1px 4px rgba(0,0,0,.25);padding:14px 10px;font-size:7.5px;color:#222;line-height:15px}
.map-card b{display:block;line-height:12px}
.map-card .x{position:absolute;right:9px;top:4px;font-size:11px}
.map-pin{left:617px;top:171px}

/* footer */
.site-footer{top:2091px;height:415px;background:var(--footer);color:var(--white)}
.site-footer .brand{left:233px;top:90px}
.site-footer .brand-name{color:var(--white)}
.footer-links{left:233px;top:140px;display:grid;grid-template-columns:132px 108px;column-gap:0}
.footer-links a{display:block;color:#e6e9f0;text-decoration:none;font-size:11px;padding:6px 0 6px 18px;border-bottom:1px solid #1f2c48;width:125px;position:relative;height:30px}
.footer-links a::before{content:"";position:absolute;left:2px;top:11px;border-left:5px solid var(--gold);border-top:3.5px solid transparent;border-bottom:3.5px solid transparent}
.footer-head{font-family:Montserrat,sans-serif;font-weight:600;font-size:14px;display:flex;align-items:center;gap:10px}
.footer-head::after{content:"";flex:1;height:1px;background:#2a3754}
.follow{left:233px;top:258px;width:293px}
.socials{left:236px;top:297px;display:flex;gap:9px}
.socials span{width:38px;height:38px;border-radius:50%;background:#14213b;display:block}
.socials span:first-child{background:var(--gold)}
.reach{left:547px;top:90px;width:418px}
.form{left:547px;top:126px;width:418px}
.field{position:absolute;background:var(--white);height:30px;font-size:7.5px;color:#888;padding:10px 10px}
.send{position:absolute;left:0;top:216px;width:418px;height:34px;background:var(--gold);font-family:Montserrat,sans-serif;font-weight:600;font-size:11px;padding:10px 18px;color:var(--white)}
.send svg{position:absolute;right:12px;top:10px}
.legal{top:2506px;height:88px;background:var(--footer);border-top:1px solid #1c2842;color:#8a93a8;font-size:8.5px;text-align:center;padding-top:36px}
</style>
</head>
<body>

<div class="band topbar" style="height:36px">
  <div class="abs mail">
    <svg width="10" height="8" viewBox="0 0 10 8"><rect x=".5" y=".5" width="9" height="7" fill="none" stroke="#fff"/><path d="M.5 .5L5 4.5 9.5 .5" fill="none" stroke="#fff"/></svg>
    clients@welbycounsel.example
  </div>
  <div class="abs addr">
    <svg width="8" height="10" viewBox="0 0 8 10"><path d="M4 9.5C1.5 6.5.5 5 .5 3.5a3.5 3.5 0 017 0C7.5 5 6.5 6.5 4 9.5z" fill="none" stroke="#fff"/><circle cx="4" cy="3.5" r="1.2" fill="#fff"/></svg>
    48-210 Palena Road, Suite 208, Kailua Kona, Hawaii 96740.
  </div>
  <a class="abs direction">Get Direction
    <svg width="12" height="8" viewBox="0 0 12 8"><path d="M0 4h10M7 1l3 3-3 3" fill="none" stroke="#fff" stroke-width="1.3"/></svg>
  </a>
</div>

<header class="masthead">
  <div class="abs brand">
    <div class="brand-name">MERIDIAN CREST LEGAL GROUP</div>
    <div class="brand-tag">Divorce and Personal Injury Lawyers</div>
  </div>
  <div class="abs call">
    <div class="call-ring">
      <svg width="14" height="14" viewBox="0 0 24 24"><path d="M6.6 10.8a15 15 0 006.6 6.6l2.2-2.2c.3-.3.7-.4 1-.2 1.1.4 2.3.6 3.6.6.6 0 1 .4 1 1V20c0 .6-.4 1-1 1A17 17 0 013 4c0-.6.4-1 1-1h3.5c.6 0 1 .4 1 1 0 1.3.2 2.5.6 3.6.1.3 0 .7-.2 1z" fill="var(--gold)"/></svg>
    </div>
    <div>
      <div class="call-label">Call For Your Free Appointment</div>
      <div class="call-number">+1.808.555.0148</div>
    </div>
  </div>
</header>

<nav class="mainnav">
  <ul>
    <li class="current">HOME</li><li>ABOUT US</li><li>PRACTICE AREAS</li><li>ATTORNEYS</li><li>BLOG</li><li>CONTACT US</li>
  </ul>
  <a class="abs cta">FREE CONSULTATION</a>
</nav>

<section class="hero">
  <div class="hero-photo" role="img" aria-label="Lawyer's hand resting on an open law book beside a wooden gavel"></div>
  <div class="abs hero-box">
    <div class="frame"></div>
    <p style="top:30px">Kona Lawyers of MCLG -Legal kōkua with aloha.</p>
    <p style="top:62px">Over 70 years of combined practice, specializing in:</p>
    <h1>Personal Injury, Family &amp; Divorce<br>Child Custody</h1>
    <p style="top:135px;line-height:15px">Dedicated to making sure you receive the care and<br>attention you need.</p>
  </div>
</section>

<section class="about">
  <div class="abs eyebrow-block">
    <div class="eyebrow">WHO WE ARE</div>
    <h2>ABOUT THE KONA LAWYERS OF MCLG</h2>
  </div>
  <h3 class="abs">Lawyers Serving the Big Island and Neighboring Islands</h3>
  <div class="abs copy">
    <p>The experienced attorneys in the Meridian Crest Legal Group's Kailua Kona, Hawaii office provide clients with a wide range of litigation expertise, including legal claims involving divorce &amp; family, personal injury, toxic exposures, intellectual property, and real estate.</p>
    <p>Our Kona office also offers commercial and hospitality litigation expertise on behalf of a wide variety of clients, including restaurants, hotels, property owners, and many others. We never wish to see our clients go to court, though if there is no other option, you're in safe hands with our seasoned trial lawyers and the many years of courtroom experience behind them.</p>
  </div>
  <a class="abs btn-gold">More About Us</a>
  <div class="abs enquiry">
    <div class="q">For Any Enquiry and Question Please Call us 24/7</div>
    <div class="n">+1.808.555.0148</div>
  </div>
  <div class="abs about-photo" role="img" aria-label="Attorney in a suit reading at a desk behind brass scales of justice"><div class="frame"></div></div>
</section>

<section class="band band-navy">
  <svg class="chev" width="1200" height="156"><polygon points="590,0 620,78 590,156 600,156 632,78 600,0" fill="#1a2c7c"/></svg>
  <div class="abs lead" style="top:50px">Call us now No Recovery, No Fee</div>
  <div class="abs headline" style="top:68px">FREE CONSULTATION</div>
  <div class="abs phone-disc" style="top:55px;background:var(--gold)">
    <svg width="20" height="20" viewBox="0 0 24 24"><path d="M6.6 10.8a15 15 0 006.6 6.6l2.2-2.2c.3-.3.7-.4 1-.2 1.1.4 2.3.6 3.6.6.6 0 1 .4 1 1V20c0 .6-.4 1-1 1A17 17 0 013 4c0-.6.4-1 1-1h3.5c.6 0 1 .4 1 1 0 1.3.2 2.5.6 3.6.1.3 0 .7-.2 1z" fill="none" stroke="#fff" stroke-width="1.4"/></svg>
  </div>
  <div class="abs big-number" style="top:55px">+1.808.555.0148</div>
</section>

<section class="practice">
  <div class="abs section-eyebrow">WHAT WE DO</div>
  <h2 class="abs">OUR PRACTICE AREAS</h2>
  <article class="abs area" style="left:233px">
    <div class="pic" role="img" aria-label="Older couple sitting together reviewing papers at home" style="background:linear-gradient(135deg,#e8ddd0,#b48b5e 55%,#7a86a8)"></div>
    <h3>FAMILY &amp; DIVORCE</h3>
    <p>Our lawyers handle all aspects of family law on the Big Island and neighboring islands. We have more than 70 years of combined experience handling divorce</p>
  </article>
  <article class="abs area" style="left:421px">
    <div class="pic" role="img" aria-label="Injured person with an arm in a sling, black and white" style="background:linear-gradient(135deg,#ddd,#555 50%,#999)"></div>
    <h3>PERSONAL INJURY</h3>
    <p>Dealing with personal injury and wrongful death claims is hard enough, so the lawyers of MCLG are here to make things as easy on you as possible.</p>
  </article>
  <article class="abs area" style="left:609px">
    <div class="pic" role="img" aria-label="Glass office tower against a pale sky" style="background:linear-gradient(160deg,#e9eef3,#8fa3b8 50%,#43566d)"></div>
    <h3>CORPORATE &amp; INTELLECTUAL PROPERTY</h3>
    <p>The attorneys at MCLG have been helping Big Island business owners with all their legal needs, so they can stay focused on what matters.</p>
  </article>
  <article class="abs area" style="left:796px">
    <div class="pic" role="img" aria-label="Large house behind green lawn and trees" style="background:linear-gradient(180deg,#5d88c4 0%,#a9c3e0 30%,#3f6e2c 55%,#6bab3a 100%)"></div>
    <h3>REAL ESTATE</h3>
    <p>Our lawyers work with home owners, buyers and property developers to ensure timely handling of all legal aspects involved in real estate.</p>
  </article>
</section>

<section class="map">
  <div class="map-fill" role="img" aria-label="Street map of Kailua Kona showing the office location near the coast"></div>
  <div class="abs map-card">
    <span class="x">×</span>
    <b>Kona Lawyers of Meridian Crest<br>Legal Group</b>
    48-210 Palena Road, Suite 208<br>Kailua Kona, Hawaii 96740.<br>
    <span style="display:block;margin-top:6px">+1.808.555.0148</span>
    <span style="display:block;margin-top:4px">clients@welbycounsel.example</span>
  </div>
  <svg class="abs map-pin" width="14" height="22" viewBox="0 0 14 22"><path d="M7 21C2.5 14 .5 11 .5 7a6.5 6.5 0 0113 0c0 4-2 7-6.5 14z" fill="#e53935"/><circle cx="7" cy="7" r="2.3" fill="#a11"/></svg>
</section>

<section class="band band-gold">
  <svg class="chev" width="1200" height="145"><polygon points="592,0 1200,0 1200,145 598,145 636,72" fill="#b98b2d"/></svg>
  <div class="abs lead" style="top:52px">Call us now No Recovery, No Fee</div>
  <div class="abs headline" style="top:70px">FREE CONSULTATION</div>
  <div class="abs phone-disc" style="top:56px;background:var(--navy)">
    <svg width="20" height="20" viewBox="0 0 24 24"><path d="M6.6 10.8a15 15 0 006.6 6.6l2.2-2.2c.3-.3.7-.4 1-.2 1.1.4 2.3.6 3.6.6.6 0 1 .4 1 1V20c0 .6-.4 1-1 1A17 17 0 013 4c0-.6.4-1 1-1h3.5c.6 0 1 .4 1 1 0 1.3.2 2.5.6 3.6.1.3 0 .7-.2 1z" fill="none" stroke="#fff" stroke-width="1.4"/></svg>
  </div>
  <div class="abs big-number" style="top:56px">+1.808.555.0148</div>
</section>

<footer class="site-footer">
  <div class="abs brand">
    <div class="brand-name">MERIDIAN CREST LEGAL GROUP</div>
    <div class="brand-tag">Divorce and Personal Injury Lawyers</div>
  </div>
  <div class="abs footer-links">
    <a>Home</a><a>Attorneys</a>
    <a>About us</a><a>Blog</a>
    <a>Practice Areas</a><a>Contact Us</a>
  </div>
  <div class="abs follow footer-head">FOLLOW US</div>
  <div class="abs socials" aria-label="Social profiles"><span></span><span></span><span></span><span></span></div>
  <div class="abs reach footer-head">REACH OUT TO US</div>
  <div class="abs form">
    <div class="field" style="left:0;top:0;width:204px">First Name</div>
    <div class="field" style="left:215px;top:0;width:203px">Last Name</div>
    <div class="field" style="left:0;top:43px;width:204px">Email</div>
    <div class="field" style="left:215px;top:43px;width:203px">Subject</div>
    <div class="field" style="left:0;top:87px;width:418px;height:79px">Message</div>
    <div class="send">SEND MESSAGE
      <svg width="16" height="12" viewBox="0 0 16 12"><rect width="16" height="12" rx="1" fill="#fff"/><path d="M0 1l8 6 8-6" fill="none" stroke="var(--gold)" stroke-width="1.4"/></svg>
    </div>
  </div>
</footer>

<div class="band legal">Copyright © 2019 Meridian Crest Legal Group. All Rights Reserved</div>

</body>
</html>
```